Rollin’ Free Bailbonds Outdoor lighted sign

I am getting a sign outside of my office building that lights up at night. The size of the sign is 7'×11"3/4 width
3'×11"3/4 height

I need to design how I want the sign to look. I want it to be very catchy so people who pass by in their cars will remember the sign. Especially the business name. I want the sign to be very memorable. The business name is important for people to remember as we have several competitors. I would love something fun and eye catching. At this business all women work here so we are not sure if we want something fun and spicy or more professional. We aren’t sure which one that we want and can’t wait to see the designs! I do not have a logo.

Target Market(s)

To catch people’s eye. Exposure

Industry/Entity Type

Bailbonds

Font styles to use
Serif

Requirements
Must have
• Rollin’ Free Bailbonds 715-382-9067
Nice to have
• Fast Release 24 Hours Any County

```html
<!DOCTYPE html>
<html lang="en">
<head>
<meta charset="utf-8">
<title>Rollin’ Free Bailbonds – Lighted Sign</title>
<link href="https://fonts.googleapis.com/css2?family=Merriweather:wght@900&family=Open+Sans:wght@800&display=swap" rel="stylesheet">
<style>
  :root {
    --board: #616161;
    --sign-black: #000000;
    --sign-red: #ff0000;
    --sign-white: #ffffff;
    --label: #ffffff;
  }
  html, body {
    margin: 0;
    padding: 0;
    width: 1200px;
    height: 1200px;
    overflow: hidden;
    background: var(--board);
  }
  .board {
    position: relative;
    width: 1200px;
    height: 1200px;
  }
  .size-label {
    position: absolute;
    margin: 0;
    font-family: "Open Sans", sans-serif;
    font-weight: 800;
    color: var(--label);
    transform: translateX(-50%);
    white-space: nowrap;
    line-height: 1;
  }
  .size-label--wide { left: 505px; top: 338px; font-size: 37px; }
  .size-label--tall { left: 1002px; top: 182px; font-size: 28px; }
  .sign {
    position: absolute;
    display: block;
    filter: drop-shadow(3px 3px 2px rgba(0,0,0,0.45));
  }
  .sign--wide { left: 123px; top: 397px; width: 743px; height: 442px; }
  .sign--tall { left: 919px; top: 246px; width: 189px; height: 742px; }
  .sign text {
    font-family: "Merriweather", serif;
    font-weight: 900;
    text-anchor: middle;
  }
  .txt-name { fill: var(--sign-white); }
  .txt-front { fill: var(--sign-white); }
  .txt-back { fill: var(--sign-black); stroke: var(--sign-white); stroke-width: 1.2; }
  .txt-dark { fill: var(--sign-black); }
  .band-black { fill: var(--sign-black); }
  .band-red { fill: var(--sign-red); }
  .cuffs { fill: var(--sign-red); stroke: var(--sign-black); stroke-width: 8; }
  .pill-outline { fill: var(--sign-black); }
  .pill { fill: var(--sign-white); }
</style>
</head>
<body>
<main class="board">

  <p class="size-label size-label--wide">Size: 7'×11"3/4</p>
  <p class="size-label size-label--tall">Size: 3'×11"3/4</p>

  <!-- Wide sign -->
  <svg class="sign sign--wide" viewBox="0 0 743 442" aria-label="Rollin’ Free Bailbonds wide sign">
    <rect class="band-black" x="0" y="0" width="743" height="325"/>
    <rect class="band-red" x="0" y="325" width="743" height="117"/>

    <g class="business-name">
      <text class="txt-name" x="371" y="102" font-size="78" textLength="288" lengthAdjust="spacingAndGlyphs">ROLLIN’</text>
      <text class="txt-name" x="371" y="183" font-size="78" textLength="569" lengthAdjust="spacingAndGlyphs">FREE BAILBONDS</text>
    </g>

    <g class="phone">
      <text class="txt-back" x="375" y="265" font-size="72" textLength="487" lengthAdjust="spacingAndGlyphs">715-382-9067</text>
      <text class="txt-front" x="371" y="261" font-size="72" textLength="487" lengthAdjust="spacingAndGlyphs">715-382-9067</text>
    </g>

    <rect class="pill-outline" x="171" y="291" width="401" height="69" rx="34.5"/>
    <rect class="pill" x="179" y="299" width="385" height="53" rx="26.5"/>
    <text class="txt-dark" x="371" y="337" font-size="33" textLength="252" lengthAdjust="spacingAndGlyphs">FAST RELEASE</text>

    <rect class="cuffs" role="img" aria-label="Red handcuffs illustration" x="25" y="257" width="123" height="104" rx="48"/>
    <rect class="cuffs" role="img" aria-label="Red handcuffs illustration" x="606" y="257" width="150" height="104" rx="48"/>

    <text class="txt-dark" x="365" y="422" font-size="52" textLength="564" lengthAdjust="spacingAndGlyphs">24 HOURS ANY COUNTY</text>
  </svg>

  <!-- Tall sign -->
  <svg class="sign sign--tall" viewBox="0 0 189 742" aria-label="Rollin’ Free Bailbonds tall sign">
    <rect class="band-black" x="0" y="0" width="189" height="365"/>
    <rect class="band-red" x="0" y="365" width="189" height="377"/>

    <g class="business-name">
      <text class="txt-name" x="95" y="61" font-size="41" textLength="154" lengthAdjust="spacingAndGlyphs">ROLLIN’</text>
      <text class="txt-name" x="95" y="106" font-size="41" textLength="100" lengthAdjust="spacingAndGlyphs">FREE</text>
      <text class="txt-name" x="95" y="153" font-size="41" textLength="92" lengthAdjust="spacingAndGlyphs">BAIL</text>
      <text class="txt-name" x="95" y="198" font-size="41" textLength="127" lengthAdjust="spacingAndGlyphs">BONDS</text>
    </g>

    <g class="phone">
      <text class="txt-back" x="97" y="246" font-size="41" textLength="154" lengthAdjust="spacingAndGlyphs">715-382</text>
      <text class="txt-front" x="95" y="244" font-size="41" textLength="154" lengthAdjust="spacingAndGlyphs">715-382</text>
      <text class="txt-back" x="97" y="293" font-size="41" textLength="96" lengthAdjust="spacingAndGlyphs">9067</text>
      <text class="txt-front" x="95" y="291" font-size="41" textLength="96" lengthAdjust="spacingAndGlyphs">9067</text>
    </g>

    <rect class="cuffs" role="img" aria-label="Red handcuffs illustration" x="4" y="316" width="181" height="134" rx="60"/>

    <text class="txt-front" x="94.5" y="500" font-size="31" textLength="88" lengthAdjust="spacingAndGlyphs">FAST</text>
    <text class="txt-front" x="94.5" y="535" font-size="31" textLength="153" lengthAdjust="spacingAndGlyphs">RELEASE</text>

    <text class="txt-dark" x="94.5" y="595" font-size="46" textLength="52" lengthAdjust="spacingAndGlyphs">24</text>
    <text class="txt-dark" x="94.5" y="640" font-size="46" textLength="141" lengthAdjust="spacingAndGlyphs">HOURS</text>
    <text class="txt-dark" x="94.5" y="684" font-size="46" textLength="91" lengthAdjust="spacingAndGlyphs">ANY</text>
    <text class="txt-dark" x="94.5" y="729" font-size="46" textLength="169" lengthAdjust="spacingAndGlyphs">COUNTY</text>
  </svg>

</main>
</body>
</html>
```